Website for Company to help with House Restoration from Hurricane Damage

Crisp, Clean and Professional!

I need a FRONT page for a website. I need it created in photoshop with the layers intact. We DO NOT need the HTML or DRB for the site. Simply the design. Any fonts you use will need to be included if they are not standard. Please make sure any fonts you use in the body of the text are available for use on Google Fonts.

I have attached a word doc that lists the menu items and additional instructions.

A little about the company - after Hurricane Marlow - DRB developed a system which allows the house to be raised, the Tremlets installed, and the house reset on the Tremlets without the expense of moving the house or driving new pilings. This option can be installed in a matter of days with limited space and at a lower construction cost.

Please refer to the attached musthaves.doc and images that are included.

The main page must incorporate the menu, the attached photos w/ text underneath (text is in the word doc attached), and the text included in the word doc.

Standard footer with contact info as well.

If you have questions please contact us!
Updates

Designs are due by Friday! We will pick one this weekend.  We are unable to change it from 10 days to 5.  Thank you!!!

Target Market(s)

People who lost their homes or businesses due to a hurricane.

Industry/Entity Type

Construction

Requirements
Must have
• See attached musthaves.doc

```html
<!DOCTYPE html>
<html lang="en">
<head>
<meta charset="utf-8">
<title>Harborline Structural Systems, LLC</title>
<link rel="stylesheet" href="https://fonts.googleapis.com/css2?family=Open+Sans:wght@300;400&family=Roboto+Condensed:wght@700&family=Lobster&display=swap">
<style>
  :root {
    --orange: #e05a1a;
    --orange-dark: #c84c10;
    --band-green: #b9d092;
    --band-green-light: #c6d9a3;
    --rule-green: #7f9a5a;
    --footer-green: #788a54;
    --footer-rule: #c4d3a0;
    --link-green: #6e8a4a;
    --text: #5a5a5a;
    --nav-text: #3a3a3a;
    --white: #ffffff;
  }
  * { margin: 0; padding: 0; box-sizing: border-box; }
  html, body { width: 1200px; height: 1130px; overflow: hidden; background: var(--white); }
  body { position: relative; font-family: "Open Sans", sans-serif; }

  .site-header { position: absolute; left: 0; top: 0; width: 1200px; height: 120px; border-bottom: 5px solid var(--rule-green); background: var(--white); }
  .brand { position: absolute; left: 174px; top: 28px; display: flex; flex-direction: column; align-items: center; gap: 10px; }
  .brand-mark { width: 44px; height: 44px; border-radius: 50%; background: var(--rule-green); }
  .brand-name { font-family: "Roboto Condensed", sans-serif; font-weight: 700; font-size: 13px; color: var(--nav-text); }

  .main-nav { position: absolute; left: 462px; top: 50px; display: flex; align-items: center; }
  .main-nav a { font-family: "Roboto Condensed", sans-serif; font-weight: 700; font-size: 12px; color: var(--nav-text); text-decoration: none; text-transform: uppercase; padding: 0 8px; line-height: 29px; }
  .main-nav a.is-active { background: linear-gradient(#f07a2a, var(--orange-dark)); color: var(--white); border-radius: 3px; padding: 0 12px; margin-right: 3px; }

  .hero-band { position: absolute; left: 0; top: 125px; width: 1200px; height: 364px; background: radial-gradient(circle at 50% 40%, var(--band-green-light), var(--band-green)); }
  .hero-band svg { position: absolute; left: 0; bottom: -6px; }

  .hero-frame { position: absolute; left: 175px; top: 171px; width: 847px; height: 408px; background: var(--white); border: 1px solid #ddd; padding: 6px; box-shadow: 0 14px 10px -10px rgba(0,0,0,0.35); }
  .hero-photo { position: relative; width: 832px; height: 394px; background: linear-gradient(#a7869a 0%, #d89a8c 18%, #7f7688 30%, #5e6377 55%, #6f7688 75%, #4f566a 100%); }
  .hero-caption { position: absolute; left: 0; right: 0; bottom: 16px; text-align: center; font-family: "Lobster", cursive; font-size: 43px; line-height: 47px; color: var(--white); text-shadow: 0 1px 3px rgba(0,0,0,0.4); }

  .intro { position: absolute; left: 176px; top: 618px; width: 843px; }
  .intro h1 { font-weight: 300; font-size: 40px; color: var(--orange); letter-spacing: 0.2px; line-height: 50px; margin-bottom: 5px; }
  .intro p { font-weight: 300; font-size: 13.7px; line-height: 25.7px; color: var(--text); text-align: justify; margin-bottom: 25.7px; }
  .intro .highlight { color: var(--orange); font-weight: 400; }
  .intro a { color: var(--link-green); font-weight: 400; }

  .site-footer { position: absolute; left: 0; top: 1013px; width: 1200px; height: 117px; background: var(--footer-green); border-top: 6px solid var(--footer-rule); padding: 27px 0 0 175px; color: var(--white); font-size: 12px; line-height: 26px; }
  .site-footer a { color: var(--white); }
</style>
</head>
<body>
  <header class="site-header">
    <div class="brand">
      <span class="brand-mark"></span>
      <span class="brand-name">Harborline Structural Systems, LLC</span>
    </div>
    <nav class="main-nav">
      <a class="is-active" href="#">Home</a>
      <a href="#">Services</a>
      <a href="#">About Us</a>
      <a href="#">Product Specifications</a>
      <a href="#">Design Documentation</a>
      <a href="#">Contact Us</a>
    </nav>
  </header>

  <div class="hero-band">
    <svg width="1200" height="8" viewBox="0 0 1200 8" aria-hidden="true">
      <polyline fill="none" stroke="#ffffff" stroke-width="6" points="0,8 6,2 12,8 18,2 24,8 30,2 36,8 42,2 48,8 54,2 60,8 66,2 72,8 78,2 84,8 90,2 96,8 102,2 108,8 114,2 120,8 126,2 132,8 138,2 144,8 150,2 156,8 162,2 168,8 174,2 180,8 1020,8 1026,2 1032,8 1038,2 1044,8 1050,2 1056,8 1062,2 1068,8 1074,2 1080,8 1086,2 1092,8 1098,2 1104,8 1110,2 1116,8 1122,2 1128,8 1134,2 1140,8 1146,2 1152,8 1158,2 1164,8 1170,2 1176,8 1182,2 1188,8 1194,2 1200,8"/>
    </svg>
  </div>

  <div class="hero-frame">
    <div class="hero-photo" role="img" aria-label="Photo of a parent and small child on a beach at sunset, with boats on the water behind them">
      <p class="hero-caption">Rebuild Safer, Stronger, Better to build new<br>lasting memories</p>
    </div>
  </div>

  <main class="intro">
    <h1>HARBORLINE STRUCTURAL SYSTEMS</h1>
    <p>Systems for extending the height of existing piles are not available on today’s market.&nbsp; <span class="highlight">Harborline Structural Systems, LLC (DRB)</span> has developed two systems to allow for Piles to be extended that provide superior structural support without corrosion and maintenance concerns.&nbsp; We provided two systems, a complete system, Pile Cap Extension Tremlets, and Pile Splice.&nbsp; These two systems allow a home to be raised to by up to 54”, higher extensions possible with additional design consideration for lateral support. Shown below is the full Piling Extension system, which connects to the top of the existing pile. The system modular and can be cut to meet specific needs of the home.</p>
    <p>Our Patented Piling system has been designed to withstand the corrosive environment of beach communities. The salt water and windblown sand corrodes unprotected materials, and yes, even stainless steel. Our system utilizes a high strength carbon fiber material that is corrosion proof from salt water and UV proof.&nbsp; The system will not erode, decay or loose strength over time. The system has three installation conditions, for raising a house on existing pilings, repairing damaged pilings, and for connecting new pilings to floor joists in new construction. <a href="#">The three options are generally described here</a>.</p>
  </main>

  <footer class="site-footer">
    <p>Harborline Structural Systems, LLC - PO Box 48120,&nbsp; Millbrook Valley, PA 18000-0410 -(555) 014-2290&nbsp; -</p>
    <p>Email: <a href="#">sales@harborlinestructural.example</a></p>
  </footer>
</body>
</html>
```